Business Card Design for digital storytelling business

I need a business card for a workshop/consulting/coaching business.

Company Name: The Bright Harbor

Tagline: Modern ways to keep family memories

What we do: Through workshops, webinars, and coaching we teach you how to capture, tell and share your important memories and stories using readily available digital tools. We will help you tell your life story in a format to share with your family now and in the future.
Updates

I just received a toll free number that I would like included on the designs. If the addition of a phone number would significantly alter your design, please submit an altered version. The number is 877-512-6098

Target Market(s)

Adults in US between ages of 35-70 interested in capturing, preserving and sharing memories and life stories in a digital format.
Could include the following:

-People touched by illness or tragedy who need to tell their own or a loved one's life story
-Grandparents wanting to share stories and wisdom with grandchildren living far away
-People with aging parents who want to capture their stories in a format to pass on to their children
-Alzheimer's patients and their families
-People wanting to transfer analog photos to digital; or wanting to organize digital photos into something that tells a story

Industry/Entity Type

Digital

Requirements
Must have
• Must include business name, logo, tagline

Contact information (see file)
Social media information

Fonts easily readable by aging eyes. Good contrast.

Nice to have
• Color preferences: blue, green, yellow/gold
Blue denotes the calm, non-pressured way that I teach. It is for the healing that comes from telling your story. It represents time and space that are bridged in the digital environment.
Green is for growth, the future, the family tree, Vines that grow and branch and connect the generations and our hearts.
Yellow/gold is for the legacy of wisdom in our lives and stories. It is for the light of truth we bring to the world by sharing our stories.
Should not have
• No old-style, script fonts.
No Times New Roman

```html
<!DOCTYPE html>
<html lang="en">
<head>
<meta charset="utf-8">
<title>The Bright Harbor – Business Card</title>
<link href="https://fonts.googleapis.com/css2?family=Montserrat:wght@400;500;600;700&display=swap" rel="stylesheet">
<style>
  :root{
    --cream:#ead5a2;
    --navy:#364272;
    --green:#2f9a48;
    --white:#ffffff;
    --ink:#2b3560;
    --stage:#e9e9ec;
  }
  *{box-sizing:border-box;margin:0;padding:0}
  html,body{width:1200px;height:897px;overflow:hidden}
  body{
    background:var(--stage);
    font-family:"Montserrat",Arial,sans-serif;
    display:flex;align-items:center;justify-content:center;gap:36px;
  }
  .card{
    position:relative;width:550px;height:334px;border-radius:26px;overflow:hidden;
    box-shadow:0 6px 18px rgba(0,0,0,.18);flex:none;
  }
  /* front */
  .card--front{background:var(--cream);color:var(--ink)}
  .front-frame{
    position:absolute;inset:18px;border:2.5px solid var(--green);border-radius:22px;
  }
  .front-tab{
    position:absolute;top:0;right:96px;width:46px;height:40px;
    background:var(--green);border-radius:0 0 12px 12px;
  }
  .name-band{
    position:absolute;left:0;top:66px;width:255px;height:36px;
    background:var(--navy);border-radius:0 18px 18px 0;
  }
  .name-band::before,.name-band::after{
    content:"";position:absolute;top:0;bottom:0;width:2px;background:var(--cream);
  }
  .name-band::before{left:10px}
  .name-band::after{left:16px}
  .person{position:absolute;left:272px;top:54px}
  .person-name{font-size:20px;font-weight:600;letter-spacing:.5px;color:var(--navy);line-height:1.1}
  .person-role{font-size:12px;font-weight:600;letter-spacing:1px;color:var(--navy);margin-top:3px}
  .brand{position:absolute;left:268px;top:128px;display:flex;align-items:center;gap:12px}
  .brand-mark{width:28px;height:28px;background:var(--navy);flex:none}
  .brand-name{font-size:19px;font-weight:600;color:var(--green);line-height:1;white-space:nowrap}
  .brand-tagline{font-size:7px;font-weight:600;letter-spacing:.5px;color:var(--navy);margin-top:5px;text-transform:uppercase;white-space:nowrap}
  .address{position:absolute;left:42px;top:212px;font-size:13px;font-weight:500;line-height:1.35;color:var(--ink);font-style:normal}
  .contacts{position:absolute;left:236px;top:204px;list-style:none;font-size:11px;color:var(--ink)}
  .contacts li{display:flex;align-items:center;gap:8px;height:19px}
  .contacts svg{width:11px;height:11px;fill:var(--ink);flex:none}
  /* back */
  .card--back{background:var(--navy);color:var(--white)}
  .back-frame{position:absolute;inset:18px;border:2px solid var(--white);border-radius:22px}
  .back-brand{position:absolute;inset:0;display:flex;align-items:center;justify-content:center;gap:14px}
  .back-brand .brand-mark{background:transparent;border:2px solid var(--white);width:32px;height:32px}
  .back-brand .brand-name{color:var(--white);font-size:24px}
  .back-brand .brand-tagline{color:var(--white);font-size:8px}
</style>
</head>
<body>
  <section class="card card--front" aria-label="Business card front">
    <div class="front-frame"></div>
    <div class="front-tab"></div>
    <div class="name-band"></div>
    <div class="person">
      <div class="person-name">DANA WHITFIELD</div>
      <div class="person-role">GENERAL MANAGER</div>
    </div>
    <div class="brand">
      <span class="brand-mark"></span>
      <div>
        <div class="brand-name">The Bright Harbor</div>
        <div class="brand-tagline">Modern ways to keep family memories</div>
      </div>
    </div>
    <address class="address">42 Lantern Road,<br>Suite 3 West</address>
    <ul class="contacts">
      <li><svg viewBox="0 0 24 24"><path d="M6.6 10.8a15 15 0 0 0 6.6 6.6l2.2-2.2c.3-.3.7-.4 1-.2 1.1.4 2.3.6 3.6.6.6 0 1 .4 1 1V20c0 .6-.4 1-1 1A17 17 0 0 1 3 4c0-.6.4-1 1-1h3.5c.6 0 1 .4 1 1 0 1.3.2 2.5.6 3.6.1.3 0 .7-.2 1z"/></svg>877-512-6098</li>
      <li><svg viewBox="0 0 24 24"><path d="M7 1h10a2 2 0 0 1 2 2v18a2 2 0 0 1-2 2H7a2 2 0 0 1-2-2V3a2 2 0 0 1 2-2zm0 3v14h10V4z"/></svg>877-512-6098</li>
      <li><svg viewBox="0 0 24 24"><path d="M6 2h9v6h6v14H6zm2 10v2h10v-2zm0 4v2h10v-2z"/></svg>877-512-6098</li>
      <li><svg viewBox="0 0 24 24"><path d="M2 5h20v14H2zm2 2v.5l8 5 8-5V7z"/></svg>hello@brightharbor.com</li>
      <li><svg viewBox="0 0 24 24"><circle cx="12" cy="12" r="10"/></svg>www.brightharbor.com</li>
    </ul>
  </section>

  <section class="card card--back" aria-label="Business card back">
    <div class="back-frame"></div>
    <div class="back-brand">
      <span class="brand-mark"></span>
      <div>
        <div class="brand-name">The Bright Harbor</div>
        <div class="brand-tagline">Modern ways to keep family memories</div>
      </div>
    </div>
  </section>
</body>
</html>
```